Supplement label for Brain health

I need a design for a supplement this supplement is a brain boost supplement.

The Name is Cortiva Plus.

I have attached other labels I like. This is for 50 plus demographic so the lettering needs to be easy to read and stand out. I have attached a dummy label template that once the winner is choosen then they will get the real supplement facts etc.

Clean desgin easy to read.

This file must be finished in AI format.

Target Market(s)

50 plus 70 percent female 30 percent male

Industry/Entity Type

Supplement

Font styles to use
Other font styles liked:
• Myrid pro maybe

Requirements
Must have
• easy to read text so no colors that hide text or hard to read.

```html
<!DOCTYPE html>
<html lang="en">
<head>
<meta charset="utf-8">
<title>Cortiva Plus – Brain Boost Supplement Label</title>
<link rel="stylesheet" href="https://fonts.googleapis.com/css2?family=Archivo+Black&family=Arimo:wght@400;700&family=Open+Sans:wght@400&family=Oswald:wght@500;600&display=swap">
<style>
  :root {
    --page-bg: #2a2a2a;
    --green-light: #24543f;
    --green-dark: #0c2119;
    --gold: #e3b92a;
    --gold-light: #f6dd5a;
    --gold-deep: #b88a12;
    --white: #ffffff;
    --text-light: #f1f1f1;
  }
  * { box-sizing: border-box; margin: 0; padding: 0; }
  html, body { width: 1200px; height: 1200px; overflow: hidden; }
  body { background: var(--page-bg); position: relative; font-family: "Arimo", Arial, sans-serif; }

  .label {
    position: absolute; left: 20px; top: 391px; width: 1160px; height: 418px;
    background: radial-gradient(ellipse at 50% 50%, var(--green-light) 0%, #173a2c 55%, var(--green-dark) 100%);
    border-top: 3px solid var(--white);
    border-bottom: 4px solid var(--gold-light);
    color: var(--text-light);
  }
  .label::before {
    content: ""; position: absolute; left: 0; right: 0; top: 3px; height: 2px; background: var(--gold);
  }

  /* Left column */
  .directions { position: absolute; left: 12px; top: 24px; width: 278px; font-size: 10.2px; line-height: 1.2; text-align: justify; }
  .directions p { margin-bottom: 10px; }
  .directions strong { font-weight: 700; }
  .fda-note {
    position: absolute; left: 12px; top: 290px; width: 234px; height: 36px;
    border: 1.5px solid var(--gold); padding: 3px 5px;
    font-size: 7.2px; font-weight: 700; line-height: 1.3;
  }
  .distributor { position: absolute; left: 12px; top: 348px; font-family: "Oswald", sans-serif; font-weight: 500; font-size: 12.5px; line-height: 1.35; }

  /* Centre */
  .brand { position: absolute; left: 340px; width: 480px; top: 18px; text-align: center; }
  .brand-name {
    font-family: "Oswald", sans-serif; font-weight: 600; font-size: 64px; line-height: 1; letter-spacing: 0.5px;
    background: linear-gradient(180deg, var(--gold-light) 0%, var(--gold) 55%, var(--gold-deep) 100%);
    -webkit-background-clip: text; background-clip: text; color: transparent;
  }
  .brand-tagline { font-family: "Open Sans", sans-serif; font-size: 29px; color: var(--white); margin-top: 2px; }
  .brain-art {
    position: absolute; left: 465px; top: 136px; width: 260px; height: 190px; border-radius: 48% 52% 40% 45%;
    background: radial-gradient(ellipse at 50% 50%, #5c6a2e 0%, #8a7a22 45%, rgba(227,185,42,0.35) 80%, rgba(227,185,42,0) 100%);
  }
  .pack-info { position: absolute; left: 340px; width: 480px; top: 342px; text-align: center; font-family: "Oswald", sans-serif; font-weight: 500; font-size: 21px; line-height: 1.25; color: var(--white); }

  /* Right column */
  .facts-column { position: absolute; left: 856px; top: 26px; width: 278px; display: flex; flex-direction: column; gap: 6px; }
  .facts { border: 2px solid var(--gold); padding: 3px 5px 2px; font-size: 10px; }
  .facts h2 { font-family: "Archivo Black", sans-serif; font-weight: 400; font-size: 23px; line-height: 1.05; color: var(--white); }
  .facts .serving { line-height: 1.2; padding-left: 3px; }
  .facts .rule { height: 5px; background: var(--gold); margin: 3px 0 2px; }
  .facts .head { font-size: 8px; padding-left: 3px; }
  .facts table { width: 100%; border-collapse: collapse; }
  .facts td { border-top: 1.5px solid var(--gold); padding: 1px 0 1px 3px; line-height: 1.18; vertical-align: top; }
  .facts td.amt { text-align: right; width: 52px; padding-right: 2px; }
  .facts td.dv { width: 12px; text-align: center; }
  .facts tr.sub td { border-top: none; padding: 0 0 1px 7px; }
  .facts .footnote { border-top: 2px solid var(--gold); padding: 1px 3px 0; line-height: 1.2; }
  .facts i { font-style: italic; }
  .notes { font-size: 10px; line-height: 1.2; }
  .notes p { margin-bottom: 10px; text-align: justify; }
</style>
</head>
<body>
  <section class="label">
    <div class="directions">
      <p><strong>SUGGESTED USE:</strong> 1 capsule taken 1 to 2 times daily preferably with meals or as directed by a healthcare professional.</p>
      <p><strong>CAUTION:</strong> Do not exceed recommended dose. St. John's Wort may contribute to photosensitivity resulting in skin irritation and redness in persons exposed to strong sunlight or tanning booths. Avoid use in patients at risk of bleeding, taking anticoagulants, or with clotting disorders, based on case reports of bleeding. Discontinue use 2-3 weeks prior to some surgical and dental procedures due to increased risk of bleeding. Avoid use in couples who are trying to conceive, based on theoretical reduction of fertility. Pregnant or nursing mothers, children under 18, individuals with history of seizure, taking MAO inhibiting drugs, or with a known medical condition should consult a physician before using this or any dietary supplement. This product is manufactured and packaged in a facility which may also process milk, soy, wheat, egg, peanuts, tree nuts, fish and crustacean shellfish.</p>
    </div>
    <div class="fda-note">†These statements have not been evaluated by the Food &amp; Drug Administration. This product is not intended to diagnose, treat, cure or prevent any disease.</div>
    <div class="distributor">Distributed by:<br>Company Name<br>Full Address and Phone</div>

    <div class="brand">
      <h1 class="brand-name">CORTIVA PLUS</h1>
      <p class="brand-tagline">Brain Boost Supplement</p>
    </div>
    <div class="brain-art" role="img" aria-label="Gold line illustration of a brain"></div>
    <div class="pack-info">DIETARY SUPPLEMENT<br>30 CAPSULES</div>

    <div class="facts-column">
      <div class="facts">
        <h2>Supplement Facts</h2>
        <div class="serving">Serving Size 1 Capsule<br>Servings Per Container: 30</div>
        <div class="rule"></div>
        <div class="head">Amt Per Serv. &nbsp; %DV/RDI</div>
        <table>
          <tr><td><i>Ginkgo biloba</i> Leaf (24% extract)</td><td class="amt">50mg</td><td class="dv">*</td></tr>
          <tr><td>Phosphatidylserine 4% Complex</td><td class="amt">125mg</td><td class="dv">*</td></tr>
          <tr class="sub"><td colspan="3">(consisting of Lecithin and Phosphatidylserine)</td></tr>
          <tr><td>N-Acetyl L-Carnitine HCl</td><td class="amt">50mg</td><td class="dv">*</td></tr>
          <tr><td>St. John's Wort (0.3% extract)</td><td class="amt">250mg</td><td class="dv">*</td></tr>
          <tr class="sub"><td colspan="3">(flower heads)</td></tr>
          <tr><td>L-Glutamine</td><td class="amt">150mg</td><td class="dv">*</td></tr>
          <tr><td><i>Bacopa monnieri</i> Leaf Extract</td><td class="amt">120mg</td><td class="dv">*</td></tr>
          <tr class="sub"><td colspan="3">(20% bacosides)</td></tr>
          <tr><td>Vinpocetine (seeds)</td><td class="amt">2mg</td><td class="dv">*</td></tr>
          <tr><td>Huperzine-A (aerial plant)</td><td class="amt">10mcg</td><td class="dv">*</td></tr>
        </table>
        <div class="footnote">*Daily Value not established.</div>
      </div>
      <div class="notes">
        <p><strong>Other ingredients:</strong> Gelatin (bovine), microcrystalline cellulose, vegetable magnesium stearate, and silicon dioxide.</p>
        <p>ALLERGEN WARNING: CONTAINS SOY (LECITHIN).</p>
        <p>KEEP OUT OF THE REACH OF CHILDREN. DO NOT USE IF SAFETY SEAL IS DAMAGED OR MISSING. STORE IN A COOL, DRY PLACE.</p>
      </div>
    </div>
  </section>
</body>
</html>
```